Create a banner for me that embodies my health and well being package.

I am an intuitive counselor with a busy practice helping clients to shift their blocks and move forward in their lives.
I have created a package called '9 paths home again'
I am wanting a banner to put on my website page, facebook page and to use as a letter head in mailouts.
My ideal clients are those who want to create change in their lives and who invest money in themselves and their personal and spiritual growth.
I am different to regular life coaches as my sessions have a spiritual twist to them creating much deeper change in my clients.
I would like the banner to be mainly font with the title of the progam: 9 Paths Home Again (no other wording) (something along the lines of the Blackjack font) and that ties in with the theme of my website. I'm not sure what else I want with it and am looking for ideas.
Website:
www.quillorabalancecare.com.au
I also have a current facebook page for the business:
https://www.facebook.com/Quillora-Balance-Care-402715938846102/
(Note: I am about to drop my logo and business name and move to using my own name - the rest of the website will remain the same).
I have attached a doc with the draft of what wording will be on the website page any advertising will link to, to give you an idea of what the program is about.

Target Market(s)

People who invest money on themselves who are looking to improve their emotional well being and creating change in their life. Majority are middle aged women (also younger females and some men)

Industry/Entity Type

Health And Wellness

Font styles to use
Other font styles liked:
• I like Blackjack and Amienne. Along those lines.

Requirements
Must have
• Attractive, modern and GREAT font.
Nice to have
• Surprise me with something amazing!
• I love the colours in the 2 images I have up loaded as they represent the heart chakra colours. They could be a feature on the banner or blurred into the background.
Should not have
• Even though my work is quite spiritual I don't want it to look woo woo (meaning airy fairy spiritual stuff!)

```html
<!DOCTYPE html>
<html lang="en">
<head>
<meta charset="utf-8">
<title>9 Paths Home Again</title>
<link rel="stylesheet" href="https://fonts.googleapis.com/css2?family=Playfair+Display:wght@400&family=Great+Vibes&display=swap">
<style>
  :root {
    --bamboo-dark: #4f7a2c;
    --bamboo-mid: #8cb85a;
    --bamboo-light: #c9dfa4;
    --frame-white: #ffffff;
    --sky-top: #c9e3ee;
    --sky-mid: #e8eee0;
    --water: #a9cfe0;
    --shore: #7f9a6a;
    --band-purple: #69679e;
    --band-edge: #c2d9ae;
    --title-white: #ffffff;
    --title-green: #cfe3b4;
  }
  html, body {
    margin: 0;
    padding: 0;
    width: 1200px;
    height: 628px;
    overflow: hidden;
    background: #ffffff;
  }
  .banner {
    position: relative;
    width: 1200px;
    height: 628px;
    overflow: hidden;
  }
  .banner__art {
    position: absolute;
    inset: 0;
    display: block;
  }
  .title-number {
    font-family: "Playfair Display", Georgia, serif;
    font-size: 230px;
    fill: var(--title-white);
  }
  .title-script {
    font-family: "Great Vibes", cursive;
  }
  .title-script--white { fill: var(--title-white); font-size: 96px; }
  .title-script--green { fill: var(--title-green); font-size: 104px; }
</style>
</head>
<body>
<div class="banner">
  <svg class="banner__art" width="1200" height="628" viewBox="0 0 1200 628" xmlns="http://www.w3.org/2000/svg">
    <defs>
      <linearGradient id="bambooGrad" x1="0" y1="0" x2="1" y2="0">
        <stop offset="0" stop-color="var(--bamboo-dark)"/>
        <stop offset="0.08" stop-color="var(--bamboo-mid)"/>
        <stop offset="0.18" stop-color="var(--bamboo-light)"/>
        <stop offset="0.3" stop-color="var(--bamboo-mid)"/>
        <stop offset="0.5" stop-color="var(--bamboo-light)"/>
        <stop offset="0.7" stop-color="var(--bamboo-mid)"/>
        <stop offset="0.85" stop-color="var(--bamboo-light)"/>
        <stop offset="1" stop-color="var(--bamboo-dark)"/>
      </linearGradient>
      <linearGradient id="lakeGrad" x1="0" y1="0" x2="0" y2="1">
        <stop offset="0" stop-color="var(--sky-top)"/>
        <stop offset="0.42" stop-color="var(--sky-mid)"/>
        <stop offset="0.5" stop-color="var(--shore)" stop-opacity="0.6"/>
        <stop offset="0.56" stop-color="var(--water)"/>
        <stop offset="1" stop-color="var(--water)"/>
      </linearGradient>
      <clipPath id="photoClip">
        <rect x="192" y="77" width="786" height="474"/>
      </clipPath>
    </defs>

    <rect class="backdrop" width="1200" height="628" fill="url(#bambooGrad)" role="img" aria-label="Soft-focus green bamboo stalks"/>

    <rect class="card-frame" x="168" y="54" width="835" height="521" fill="var(--frame-white)"/>

    <g clip-path="url(#photoClip)">
      <rect class="card-photo" x="192" y="77" width="786" height="474" fill="url(#lakeGrad)" role="img" aria-label="Woman in white sitting calmly by a sunlit lake with eyes closed"/>
      <path class="band-edge" d="M192 352 C 400 275, 700 260, 978 430 L978 551 L192 551 Z" fill="var(--band-edge)"/>
      <path class="band" d="M192 362 C 400 290, 690 280, 978 452 L978 551 L192 551 Z" fill="var(--band-purple)"/>
    </g>

    <g class="title">
      <text class="title-number" x="300" y="508">9</text>
      <text class="title-script title-script--white" x="420" y="418">Paths</text>
      <text class="title-script title-script--green" x="370" y="510">Home Again</text>
    </g>
  </svg>
</div>
</body>
</html>
```